Business card design needed

My company does everything from wiring up your exisiting entertainment system, to installing a complete new system for you. We can mount your plasma on the wall, install an aerial point for you, setup some surround sound in your outdoor area or install a new cinema room in your house. Any Audio or Visual requirements you may have we can provide these for you. If you want to have a party to remember at your place or just some chilled sounds by the pool, we can give you just the right size system.

Industry/Entity Type

Entertainment

Contact Information for Business Card

The Tune Crew
Colin Pemberton
e| colin@thetunecrew.com.au
w| www.thetunecrew.com.au
m| 0412 576 208

Requirements
Must have
• The logo that i have uploaded is just a starter...something similar to this but not exact or any new suggestions you have would be great too. Colour choice we are pretty easy on we did think Red and Yellow but happy to take advice, something that stands out from the rest i guess.

```html
<!DOCTYPE html>
<html lang="en">
<head>
<meta charset="utf-8">
<title>The Tune Crew – Business Card</title>
<link rel="stylesheet" href="https://fonts.googleapis.com/css2?family=Exo+2:wght@400;500;700&display=swap">
<style>
  :root {
    --page: #f2f2f3;
    --band-grey: #6d6e72;
    --card-white: #ffffff;
    --gold: #f0b94a;
    --gold-pale: #f8e2b6;
    --gold-muted: #c9a86c;
    --royal-blue: #1b6fb5;
    --soft-blue: #8da6cd;
  }
  html, body {
    margin: 0;
    width: 1200px;
    height: 698px;
    overflow: hidden;
    background: var(--page);
  }
  .business-card {
    position: absolute;
    left: 60px;
    top: 63px;
    width: 1080px;
    height: 571px;
    display: block;
    box-shadow: 0 6px 24px rgba(0,0,0,0.18);
  }
  .band-top { fill: var(--band-grey); }
  .band-bottom { fill: var(--card-white); }
  .meter-area { fill: url(#meterTones); }
  .logo-mark { fill: var(--gold); }
  .logo-name {
    font-family: "Exo 2", sans-serif;
    font-weight: 500;
    font-size: 22px;
    fill: var(--gold);
  }
  .company-name {
    font-family: "Exo 2", sans-serif;
    font-weight: 700;
    font-size: 24px;
    letter-spacing: 1.5px;
    fill: var(--gold);
  }
  .person-name {
    font-family: "Exo 2", sans-serif;
    font-weight: 500;
    font-size: 29px;
    fill: var(--royal-blue);
  }
  .contact-line {
    font-family: "Exo 2", sans-serif;
    font-weight: 400;
    font-size: 14px;
    letter-spacing: 1.2px;
    fill: var(--gold);
  }
  .contact-line.mobile { fill: var(--soft-blue); letter-spacing: 3px; }
</style>
</head>
<body>
<svg class="business-card" viewBox="0 0 700 370" xmlns="http://www.w3.org/2000/svg">
  <defs>
    <linearGradient id="meterTones" x1="0" y1="0" x2="0" y2="1">
      <stop offset="0" stop-color="#c9a86c"/>
      <stop offset="0.45" stop-color="#f0b94a"/>
      <stop offset="1" stop-color="#f8e2b6"/>
    </linearGradient>
  </defs>

  <rect class="band-bottom" x="0" y="0" width="700" height="370"/>
  <rect class="band-top" x="0" y="0" width="700" height="227"/>

  <rect class="meter-area" x="0" y="124" width="287" height="246"
        role="img" aria-label="Sound level meter illustration in gold tones"/>

  <g class="brand-logo">
    <rect class="logo-mark" x="282" y="113" width="13" height="13"/>
    <text class="logo-name" x="302" y="126">tune crew</text>
  </g>

  <g class="contact-block">
    <text class="company-name" x="642" y="260" text-anchor="end">The Tune Crew</text>
    <text class="person-name" x="642" y="298" text-anchor="end">Colin Pemberton</text>
    <text class="contact-line" x="642" y="325" text-anchor="end">e| colin@thetunecrew.com.au</text>
    <text class="contact-line" x="642" y="342" text-anchor="end">w| www.thetunecrew.com.au</text>
    <text class="contact-line mobile" x="642" y="361" text-anchor="end">m| 0412 576 208</text>
  </g>
</svg>
</body>
</html>
```